Need a new design for Glass Cleaner label. The brand name already exists i.e. BRIXO. Pell is the company name. Looking for new design. It's application is for cleaning glasses in houses, cars, offices e.t.c. Our product gives streak free shine and anti static effect. Images of old label design is attached. Bottle will be same as before. It's better to show a car as well in the design but not necessary. New logo's of brixo can also be designed.

Target Market(s)

Household and automobile

Industry/Entity Type

It Company

```html
<!DOCTYPE html>
<html lang="en">
<head>
<meta charset="utf-8">
<title>BRIXO Glass Cleaner Label</title>
<link rel="stylesheet" href="https://fonts.googleapis.com/css2?family=Roboto+Condensed:wght@700&family=Tinos:ital@1&display=swap">
<style>
  :root {
    --canvas-bg: #e6e8ec;
    --brand-red: #d2141e;
    --brand-red-dark: #9e0c14;
    --navy: #1d2a78;
    --royal-blue: #2f56c8;
    --sky-blue: #8fb7ee;
    --label-white: #ffffff;
    --panel-black: #111218;
  }
  html, body {
    margin: 0;
    padding: 0;
    overflow: hidden;
  }
  body {
    width: 1141px;
    height: 1200px;
    background: var(--canvas-bg);
    position: relative;
  }
  .label {
    position: absolute;
    left: 320px;
    top: 137px;
    width: 500px;
    height: 925px;
    filter: drop-shadow(0 10px 18px rgba(0,0,0,0.18));
  }
  .label-base { fill: var(--label-white); }
  .band-red { fill: var(--brand-red); }
  .band-red-shade { fill: var(--brand-red-dark); }
  .swoosh-white { fill: none; stroke: var(--label-white); stroke-width: 6; }
  .band-navy { fill: var(--navy); }
  .band-royal { fill: var(--royal-blue); }
  .streak-sky { fill: none; stroke: var(--sky-blue); stroke-width: 5; opacity: 0.9; }
  .streak-white { fill: none; stroke: var(--label-white); stroke-width: 3; opacity: 0.85; }
  .company-name {
    font-family: "Roboto Condensed", sans-serif;
    font-weight: 700;
    font-size: 58px;
    fill: var(--label-white);
  }
  .product-type {
    font-family: "Tinos", serif;
    font-style: italic;
    font-size: 36px;
    fill: var(--navy);
  }
  .brand-name {
    font-family: "Roboto Condensed", sans-serif;
    font-weight: 700;
    font-size: 132px;
    fill: var(--brand-red);
  }
</style>
</head>
<body>
  <svg class="label" viewBox="0 0 500 925" xmlns="http://www.w3.org/2000/svg">
    <defs>
      <clipPath id="label-outline">
        <path d="M0 240 C0 170 40 125 110 105 L420 20 C470 6 500 30 500 80 L500 700 C500 860 400 925 250 925 C100 925 0 860 0 720 Z"/>
      </clipPath>
      <linearGradient id="car-photo-tone" x1="0" y1="0" x2="1" y2="1">
        <stop offset="0" stop-color="#15161d"/>
        <stop offset="0.55" stop-color="#5a1016"/>
        <stop offset="1" stop-color="#101116"/>
      </linearGradient>
    </defs>

    <g clip-path="url(#label-outline)">
      <rect class="label-base" x="0" y="0" width="500" height="925"/>

      <g class="top-band">
        <path class="band-red-shade" d="M0 345 C120 250 300 225 500 255 L500 0 L0 0 Z"/>
        <path class="band-red" d="M0 320 C120 225 300 200 500 225 L500 0 L0 0 Z"/>
        <path class="swoosh-white" d="M20 300 C140 215 310 195 500 210"/>
      </g>

      <g class="side-bands">
        <path class="band-navy" d="M0 360 C60 300 120 280 170 275 C90 330 40 460 60 620 C80 760 170 850 300 925 L0 925 Z"/>
        <path class="band-royal" d="M0 420 C40 360 90 320 130 305 C70 380 50 500 75 630 C100 750 180 840 280 925 L180 925 C80 850 20 740 10 620 Z" opacity="0.85"/>
        <path class="streak-sky" d="M150 300 C80 380 70 520 110 640 C140 730 200 800 300 860"/>
        <path class="streak-white" d="M120 310 C60 400 60 530 95 640"/>
      </g>

      <path class="car-photo" role="img" aria-label="Photo of a red convertible car on a dark background"
            fill="url(#car-photo-tone)"
            d="M150 660 C210 560 340 520 500 515 L500 835 C420 880 300 885 200 860 C160 800 140 720 150 660 Z"/>

      <path class="band-navy" d="M140 870 C260 900 400 880 500 830 L500 925 L120 925 Z"/>
      <path class="streak-sky" d="M160 880 C280 905 410 880 500 845"/>
    </g>

    <text class="company-name" x="370" y="160" transform="rotate(-6 370 160)">Pell</text>
    <text class="product-type" x="205" y="360" transform="rotate(-9 205 360)">Glass Cleaner</text>
    <text class="brand-name" x="40" y="500" transform="rotate(-9 40 500)">BRIXO</text>
  </svg>
</body>
</html>
```